Veltrano Energy Business Card Design

website: www.veltranoenergy.example
Project: Business Card Design for Veltrano Energy
Name: Dorian Kettle
Title: Founder / Operations Strategist
Visual Identity & Logo:
Logo File: VEL-Logo-FullGradient-Final.png (Attached).
Color Palette: The brand relies on a distinctive Cyan (Blue) to Lime Green gradient.
Background Preference: We want a Dark Mode aesthetic (Deep Matte Black, Charcoal, or Dark Slate) to make the neon gradient of the logo pop. This feels more "tech/industrial" than a standard white card.
Design Aesthetic (The "Ops" Vibe):
Concept: "Grid & Infrastructure." We are a solar rental company, focusing on logistics and access.
Typography: White, bold sans-serif text for contact info. High contrast against the dark background.
Accents: Use the Cyan or Lime Green from the logo for thin divider lines or edge painting.
Avoid: No orange/gold (clashes with logo). No cartoon leaves.
Layout Requirements:
Front: Large, centered logo. Maybe a subtle UV gloss spot varnish over the logo icon.
Back: Name, Title, Contact Info.
Texture: Matte finish cardstock with gloss elements.
sample mock up of information on card: https://brivomarkco-my.filehost.example/:i:/g/personal/dorian_kettle_veltranoenergy_example/AbCdEfGhIjKlMnOpQrStUvWxYz012345678?e=Xy12Ab
Logo: https://brivomarkco.filehost.example/:i:/s/VeltranoEnergy/ZyXwVuTsRqPoNmLkJiHgFeDcBa9876543210?e=Pq34Cd

```html
<!DOCTYPE html>
<html lang="en">
<head>
<meta charset="utf-8">
<title>Veltrano Energy — Business Card</title>
<link rel="stylesheet" href="https://fonts.googleapis.com/css2?family=Poppins:wght@300;400;500;600&display=swap">
<style>
  :root {
    --page: #161618;
    --card: #232527;
    --card-edge: #2c2e30;
    --ink: #f2f3f3;
    --ink-soft: #c9cccd;
    --ink-dim: #8f9497;
    --cyan: #22c3d0;
    --lime: #a6d72c;
    --ring: #3a3d40;
  }
  * { box-sizing: border-box; margin: 0; padding: 0; }
  html, body {
    width: 1200px; height: 800px; overflow: hidden;
    background: var(--page);
    font-family: "Poppins", sans-serif;
    color: var(--ink);
  }
  .canvas {
    position: relative; width: 1200px; height: 800px;
    display: flex; align-items: center; justify-content: center; gap: 40px;
  }
  .card {
    position: relative; width: 540px; height: 309px;
    background: var(--card);
    border: 1px solid var(--card-edge);
    border-radius: 18px;
    overflow: hidden;
  }

  /* Front */
  .front__brand {
    position: absolute; left: 0; right: 0; top: 104px;
    display: flex; align-items: center; justify-content: center; gap: 16px;
  }
  .front__mark {
    width: 22px; height: 22px; background: var(--ink-soft);
  }
  .front__name {
    font-weight: 300; font-size: 42px; letter-spacing: 0.5px;
    color: var(--ink-soft);
  }
  .front__web {
    position: absolute; left: 0; right: 0; top: 196px;
    text-align: center;
    font-size: 12px; font-weight: 400; letter-spacing: 4px;
    color: var(--ink-soft);
  }

  /* Back */
  .back__brand {
    position: absolute; left: 38px; top: 0; height: 309px;
    display: flex; align-items: center;
  }
  .back__brand-name {
    writing-mode: vertical-rl; transform: rotate(180deg);
    font-weight: 300; font-size: 36px; letter-spacing: 0.5px;
    color: var(--cyan);
  }
  .back__details {
    position: absolute; left: 168px; top: 42px; width: 310px;
  }
  .person__name {
    font-size: 21px; font-weight: 500; line-height: 1.15;
    color: var(--lime);
  }
  .person__title {
    font-size: 12px; font-weight: 400; color: var(--ink); margin-top: 2px;
  }
  .divider {
    width: 180px; height: 1.5px; margin: 12px 0 14px;
    background: linear-gradient(90deg, var(--cyan), var(--lime));
  }
  .address {
    font-style: normal; font-size: 12px; line-height: 1.55; color: var(--ink);
  }
  .contact { list-style: none; margin-top: 12px; }
  .contact__item {
    display: flex; align-items: center; gap: 9px;
    font-size: 12px; line-height: 1.7; color: var(--ink);
  }
  .contact__icon { width: 11px; height: 11px; flex: none; }
  .offices {
    display: flex; align-items: center; gap: 8px; margin-top: 14px;
  }
  .offices__label { font-size: 12px; color: var(--ink); margin-right: 4px; }
  .offices__dot {
    width: 26px; height: 26px; border-radius: 50%;
    background: var(--ring); border: 1px solid var(--ink-dim);
  }
  .back__web {
    position: absolute; right: 14px; top: 0; height: 309px;
    display: flex; align-items: center;
  }
  .back__web-text {
    writing-mode: vertical-rl;
    font-size: 9.5px; letter-spacing: 1.6px; text-transform: uppercase;
    color: var(--cyan);
  }
</style>
</head>
<body>
  <main class="canvas">
    <section class="card front" aria-label="Card front">
      <div class="front__brand">
        <span class="front__mark"></span>
        <span class="front__name">Veltrano Energy</span>
      </div>
      <p class="front__web">www.veltranoenergy.example</p>
    </section>

    <section class="card back" aria-label="Card back">
      <div class="back__brand">
        <span class="back__brand-name">Veltrano Energy</span>
      </div>

      <div class="back__details">
        <h1 class="person__name">Dorian Kettle</h1>
        <p class="person__title">Founder / Operations Strategist</p>
        <div class="divider"></div>
        <address class="address">
          Veltrano Energy, LLC<br>
          4120 Harlow Basin Road<br>
          Marren, FL 30418
        </address>
        <ul class="contact">
          <li class="contact__item">
            <svg class="contact__icon" viewBox="0 0 11 11" aria-hidden="true">
              <rect x="1" y="1" width="9" height="9" fill="none" stroke="var(--cyan)" stroke-width="1.4"/>
            </svg>
            555.014.2297
          </li>
          <li class="contact__item">
            <svg class="contact__icon" viewBox="0 0 11 11" aria-hidden="true">
              <rect x="0.5" y="2" width="10" height="7" fill="var(--cyan)"/>
              <path d="M0.5 2 L5.5 6 L10.5 2" fill="none" stroke="var(--lime)" stroke-width="1.2"/>
            </svg>
            info@veltranoenergy.example
          </li>
        </ul>
        <div class="offices">
          <span class="offices__label">Office</span>
          <span class="offices__dot" role="img" aria-label="United States office marker"></span>
          <span class="offices__dot" role="img" aria-label="Canada office marker"></span>
          <span class="offices__dot" role="img" aria-label="United Kingdom office marker"></span>
        </div>
      </div>

      <div class="back__web">
        <span class="back__web-text">www.veltranoenergy.example</span>
      </div>
    </section>
  </main>
</body>
</html>
```